Tunnel

a graphic meme to be sent to my clients, consisting of a long angular dark tunnel with a bright light at one end; located within the bright light at the end of the tunnel is the number 2021
the illuminated (shiny silver?) 3 dimensional font message running along the left wall of the tunnel is: BE SAFE.!
the smaller font message underneath the graphic is: Best Wishes For a Healthy New Year
Lem Dortvan Mediator (also to be included nearby is a small semi-circle logo of my corporate logo).

Font styles to use
Sans Serif
Other font styles liked:
• 3 dimensional bold lettering for BE SAFE

```html
<!DOCTYPE html>
<html lang="en">
<head>
<meta charset="utf-8">
<title>Be Safe 2021 – New Year Greeting</title>
<link rel="stylesheet" href="https://fonts.googleapis.com/css2?family=Oswald:wght@500;600;700&family=Roboto+Condensed:wght@400;700&display=swap">
<style>
  :root{
    --tunnel-dark:#111111;
    --tunnel-mid:#3a3a3a;
    --light-glow:#ffffff;
    --letter-face:#a3a3a3;
    --letter-side:#1b1b1b;
    --band:#241c35;
    --band-text:#ececf0;
    --gold:#c9962e;
  }
  *{margin:0;padding:0;box-sizing:border-box}
  html,body{width:834px;height:1200px;overflow:hidden;background:var(--band)}
  .card{position:relative;width:834px;height:1200px;overflow:hidden;background:var(--band)}

  .tunnel-scene{
    position:absolute;left:0;top:0;width:834px;height:864px;
    background:
      radial-gradient(ellipse 70px 80px at 690px 470px, var(--light-glow) 0%, var(--light-glow) 55%, rgba(255,255,255,0.35) 80%, rgba(255,255,255,0) 100%),
      radial-gradient(ellipse 170px 160px at 690px 480px, rgba(200,200,200,0.35) 0%, rgba(200,200,200,0) 100%),
      radial-gradient(ellipse 420px 520px at 60px 560px, rgba(160,160,160,0.75) 0%, rgba(110,110,110,0.4) 55%, rgba(0,0,0,0) 100%),
      linear-gradient(180deg, #2a2a2a 0%, var(--tunnel-dark) 25%, #1a1a1a 60%, var(--tunnel-mid) 100%);
  }

  .headline-group{margin:0}
  .headline{
    position:absolute;font-family:"Oswald",sans-serif;font-weight:700;
    color:var(--letter-face);line-height:1;white-space:nowrap;
    text-shadow:-2px 0 var(--letter-side),-4px 0 var(--letter-side),-6px 0 var(--letter-side),
      -8px 0 var(--letter-side),-10px 0 var(--letter-side),-12px 0 var(--letter-side),
      -14px 0 var(--letter-side),-16px 0 var(--letter-side);
  }
  .headline--be{
    left:98px;top:238px;font-size:440px;letter-spacing:-6px;
    transform-origin:left center;
    transform:perspective(700px) rotateY(22deg) scaleX(0.62);
  }
  .headline--safe{
    left:408px;top:352px;font-size:230px;font-weight:600;letter-spacing:-4px;
    transform-origin:left center;
    transform:perspective(500px) rotateY(24deg) scaleX(0.36);
    text-shadow:-2px 0 var(--letter-side),-4px 0 var(--letter-side),-6px 0 var(--letter-side),
      -8px 0 var(--letter-side),-10px 0 var(--letter-side);
  }
  .year{
    position:absolute;left:634px;top:410px;width:112px;text-align:center;white-space:nowrap;
    font-family:"Oswald",sans-serif;font-weight:600;font-size:58px;line-height:1;
    color:var(--light-glow);text-shadow:0 0 3px rgba(0,0,0,0.15);
  }

  .greeting{
    position:absolute;left:0;top:864px;width:834px;height:336px;background:var(--band);
    font-family:"Roboto Condensed",sans-serif;color:var(--band-text);
  }
  .greeting__wish{
    position:absolute;left:0;top:44px;width:866px;text-align:center;white-space:nowrap;
    font-weight:700;font-size:50px;line-height:1;letter-spacing:-1px;
    transform-origin:433px 50%;transform:scaleX(0.86);
  }
  .greeting__name{
    position:absolute;left:306px;top:120px;width:300px;text-align:center;white-space:nowrap;
    font-weight:400;font-size:37px;line-height:1;
    transform-origin:center;transform:scaleX(0.92);
  }
  .firm{
    position:absolute;left:248px;top:226px;width:400px;white-space:nowrap;
    display:flex;justify-content:center;align-items:center;gap:10px;
    font-family:"Roboto Condensed",sans-serif;font-weight:400;font-size:22px;color:var(--gold);
  }
  .firm__dot{width:14px;height:14px;border-radius:50%;background:var(--gold);flex:none}
</style>
</head>
<body>
<main class="card">
  <div class="tunnel-scene" role="img" aria-label="Dark angular tunnel with a stone wall on the left and bright light at the far end"></div>
  <h1 class="headline-group" aria-label="Be Safe!">
    <span class="headline headline--be" aria-hidden="true">BE</span>
    <span class="headline headline--safe" aria-hidden="true">SAFE!</span>
  </h1>
  <div class="year">2021</div>

  <section class="greeting">
    <p class="greeting__wish">Best Wishes For a Healthy New Year</p>
    <p class="greeting__name">Lem Dortvan</p>
    <div class="firm"><span class="firm__dot"></span><span class="firm__name">Harrow Lyle Mediation</span></div>
  </section>
</main>
</body>
</html>
```